Dravel

We are openıng one huntıng showroom in Riyadh? Saudi Arabia. Company name is "DRAVEL".
Our logo designed and we need Business Card Design now.
I attached DRAVEL logo below.
Front side will English and back side will be Arabic

```html
<!DOCTYPE html>
<html lang="en">
<head>
<meta charset="utf-8">
<title>Dravel Business Card</title>
<link rel="stylesheet" href="https://fonts.googleapis.com/css2?family=Arimo:wght@400;700&display=swap">
<style>
  :root {
    --stage: #1d1e21;
    --brand-green: #17803f;
    --leaf-green: #5f9a2a;
    --paper: #ffffff;
    --ink-on-green: #ffffff;
  }
  * { box-sizing: border-box; margin: 0; padding: 0; }
  html, body { width: 1200px; height: 800px; overflow: hidden; }
  body {
    background: var(--stage);
    font-family: "Arimo", Arial, sans-serif;
    display: flex;
    align-items: center;
    justify-content: center;
    gap: 40px;
  }
  .card {
    position: relative;
    width: 540px;
    height: 310px;
    border-radius: 2px;
  }
  .card--front { background: var(--brand-green); color: var(--ink-on-green); }
  .card--back { background: var(--paper); color: var(--brand-green); }

  .brand {
    position: absolute;
    left: 40px;
    top: 150px;
    display: flex;
    align-items: center;
    gap: 10px;
  }
  .brand-mark { width: 16px; height: 16px; background: currentColor; }
  .brand-name {
    font-weight: 700;
    font-size: 50px;
    letter-spacing: 1px;
    line-height: 1;
  }

  .contact {
    position: absolute;
    left: 290px;
    top: 44px;
    width: 230px;
    font-size: 13px;
    line-height: 1.35;
  }
  .person-name { font-weight: 700; font-size: 16px; letter-spacing: 0.3px; }
  .person-role { font-size: 14px; margin-bottom: 10px; }
  .card--back .person-name .first { color: var(--leaf-green); }
  .card--back .person-role { color: var(--leaf-green); }

  .contact-group {
    display: grid;
    grid-template-columns: 16px 1fr;
    column-gap: 8px;
    row-gap: 2px;
    align-items: center;
    padding: 6px 0;
  }
  .divider {
    border-top: 2px dotted currentColor;
    opacity: 0.85;
  }
  .card--back .divider { border-top-color: var(--leaf-green); }
  .icon { width: 13px; height: 13px; fill: currentColor; }
  .web strong { font-weight: 700; }
  .address { padding-left: 24px; padding-top: 6px; }
</style>
</head>
<body>

<section class="card card--front" aria-label="Front of card">
  <div class="brand">
    <span class="brand-mark"></span>
    <span class="brand-name">DRAVEL</span>
  </div>
  <div class="contact">
    <p class="person-name">KARIM HADDAD</p>
    <p class="person-role">Founder</p>
    <div class="contact-group">
      <svg class="icon" viewBox="0 0 13 13"><rect x="3" y="0.5" width="7" height="12" rx="1.2" fill="none" stroke="currentColor" stroke-width="1.4"/></svg>
      <span>(555) 010-2040</span>
      <svg class="icon" viewBox="0 0 13 13"><rect x="3" y="1" width="7" height="4"/><rect x="1" y="5" width="11" height="7" rx="1"/></svg>
      <span>(555) 010-2041</span>
    </div>
    <div class="divider"></div>
    <div class="contact-group">
      <svg class="icon" viewBox="0 0 13 13"><rect x="0.5" y="2.5" width="12" height="8"/><path d="M0.5 2.5 L6.5 7 L12.5 2.5" fill="none" stroke="var(--brand-green)" stroke-width="1.2"/></svg>
      <span>hello@dravelmail.com</span>
      <svg class="icon" viewBox="0 0 13 13"><circle cx="6.5" cy="6.5" r="6"/><path d="M0.5 6.5h12M6.5 0.5v12M2 3.5h9M2 9.5h9" stroke="var(--brand-green)" stroke-width="0.9" fill="none"/></svg>
      <span class="web">www.<strong>dravelstore</strong>.com</span>
    </div>
    <div class="divider"></div>
    <p class="address">PO Box 450 Olaya Road<br>North District Riyadh</p>
  </div>
</section>

<section class="card card--back" aria-label="Back of card">
  <div class="brand">
    <span class="brand-mark"></span>
    <span class="brand-name">DRAVEL</span>
  </div>
  <div class="contact">
    <p class="person-name"><span class="first">KARIM</span> HADDAD</p>
    <p class="person-role">Founder</p>
    <div class="contact-group">
      <svg class="icon" viewBox="0 0 13 13"><rect x="3" y="0.5" width="7" height="12" rx="1.2" fill="none" stroke="currentColor" stroke-width="1.4"/></svg>
      <span>(555) 010-2040</span>
      <svg class="icon" viewBox="0 0 13 13"><rect x="3" y="1" width="7" height="4"/><rect x="1" y="5" width="11" height="7" rx="1"/></svg>
      <span>(555) 010-2041</span>
    </div>
    <div class="divider"></div>
    <div class="contact-group">
      <svg class="icon" viewBox="0 0 13 13"><rect x="0.5" y="2.5" width="12" height="8"/><path d="M0.5 2.5 L6.5 7 L12.5 2.5" fill="none" stroke="var(--paper)" stroke-width="1.2"/></svg>
      <span>hello@dravelmail.com</span>
      <svg class="icon" viewBox="0 0 13 13"><circle cx="6.5" cy="6.5" r="6"/><path d="M0.5 6.5h12M6.5 0.5v12M2 3.5h9M2 9.5h9" stroke="var(--paper)" stroke-width="0.9" fill="none"/></svg>
      <span class="web">www.<strong>dravelstore</strong>.com</span>
    </div>
    <div class="divider"></div>
    <p class="address">PO Box 450 Olaya Road<br>North District Riyadh</p>
  </div>
</section>

</body>
</html>
```